Web design for business website

I need a web design for a business website for one of our clients who is specialized in alarm management software. I would like you to design 3 web pages, one for each of the 3 pages. You need to process the corporate identity of our client to the web design. This means the colors of the logo (red and black) should definitely show up on all of the 3 pages. Find the logo file for the logo of our customer. To increase readability I suggest you use a white/light background. All suggestions are welcome.

Please kindly download atttached Webdesign.zip and read the project brief first. The project brief refers to all other files of the zip file. Your design must have exactly the same structure as the wireframes.
Updates

Target Market(s)

B2B, Alarm management

Industry/Entity Type

Business

Number of Pages Required

3 page

Requirements
Must have
• The web design must have exactly the same structure as the wireframes and needs to contain the colors of the company logo.

```html
<!DOCTYPE html>
<html lang="en">
<head>
<meta charset="utf-8">
<title>Veritor – Real-time reasoning solutions</title>
<link href="https://fonts.googleapis.com/css2?family=Exo+2:wght@400;500;600;800&display=swap" rel="stylesheet">
<style>
:root{
  --red:#e8491a;
  --navy:#1d1b3c;
  --navy-line:#34325a;
  --ink:#222;
  --grey:#9a9a9a;
  --line:#dcdcdc;
  --white:#fff;
}
*{box-sizing:border-box;margin:0;padding:0}
html,body{width:752px;height:1200px;overflow:hidden;background:var(--white)}
body{position:relative;font-family:"Exo 2",sans-serif;color:var(--ink)}
.abs{position:absolute}

.topbar{left:0;top:0;width:752px;height:30px;border-bottom:1px solid var(--line)}
.topbar .phone{left:62px;top:8px;font-size:10px}
.topbar .lang{left:491px;top:8px;font-size:10px;display:flex;align-items:center;gap:4px}
.search{left:537px;top:4px;width:153px;height:21px;border:1px solid var(--ink);border-radius:3px;font-size:9px;padding:4px 8px;color:#555}
.search svg{position:absolute;right:6px;top:4px}

.brand-name{left:62px;top:44px;font-weight:600;font-size:28px;color:var(--navy);line-height:1}
.brand-tag{left:62px;top:76px;font-size:9px;color:var(--navy);font-weight:500}

.btn{height:28px;font-size:10px;display:flex;align-items:center;justify-content:center;border:1px solid var(--red);border-radius:2px;color:var(--red)}
.btn-solid{background:var(--red);color:var(--white)}
.btn-account{left:457px;top:49px;width:73px}
.btn-login{left:537px;top:49px;width:73px}
.btn-signup{left:616px;top:49px;width:74px}

.mainnav{left:62px;top:97px;width:628px;height:42px;background:var(--navy);display:flex;border-radius:2px}
.mainnav a{color:var(--white);font-size:10px;text-decoration:none;display:flex;align-items:center;padding:0 13px;border-right:1px solid var(--navy-line)}
.mainnav a.active{background:var(--red);padding:0 16px}

.hero{left:0;top:157px;width:752px;height:325px;background:linear-gradient(180deg,#7d8f9c 0%,#c9a77a 45%,#6f7060 62%,#3f4a2c 78%,#5b6a63 100%)}
.hero-arrow{top:305px;width:30px;height:30px;border-radius:50%;background:#eee;display:flex;align-items:center;justify-content:center}

.welcome-title{left:0;top:516px;width:752px;text-align:center;color:var(--red);font-size:14.5px;font-weight:400}
.welcome-text{left:140px;top:543px;width:472px;text-align:center;color:var(--grey);font-size:8.6px;line-height:17.6px}
.btn-more{left:336px;top:650px;width:79px;height:27px;font-size:9px}

.divider{left:180px;top:712px;width:390px;height:8px;border-radius:50%;box-shadow:0 5px 6px -3px rgba(0,0,0,.35)}

.clients-title{left:0;top:749px;width:752px;text-align:center;color:var(--red);font-size:14px;font-weight:400}
.clients{left:62px;top:781px;display:flex;gap:5px}
.client{width:85px;height:62px;border:1px solid var(--line);border-radius:2px;display:flex;align-items:center;justify-content:center;font-size:11px;font-weight:500;color:var(--navy)}

.social-bar{left:62px;top:881px;width:628px;height:43px;display:flex;border:1px solid var(--line)}
.social{width:44px;display:flex;align-items:center;justify-content:center;font-size:9px;font-weight:500;border-right:1px solid var(--line)}
.social-first{background:var(--navy);color:var(--white)}
.email{flex:1;display:flex;align-items:center;justify-content:flex-end;padding-right:16px;font-size:12px}
.subscribe{width:176px;background:var(--red);color:var(--white);display:flex;align-items:center;justify-content:center;font-size:11px}

.footer{left:0;top:962px;width:752px;height:238px;background:var(--navy);color:var(--white)}
.footer-rule{left:0;top:41px;width:752px;height:1px;background:var(--navy-line)}
.footer-col{top:15px}
.footer-col h3{font-weight:400;color:var(--red);font-size:12.5px;margin-bottom:25px}
.footer-col li{list-style:none;font-size:9px;height:22.6px;white-space:nowrap}
.footer-base{left:62px;top:185px;width:628px;height:1px;background:var(--navy-line)}
.copyright{left:0;top:206px;width:752px;text-align:center;font-size:8.6px;word-spacing:1px}
</style>
</head>
<body>

<header>
  <div class="abs topbar">
    <span class="abs phone">T +31 (0)10 555 0142</span>
    <span class="abs lang">ENG
      <svg width="7" height="5" viewBox="0 0 7 5"><path d="M0.5 0.5 3.5 3.8 6.5 0.5" fill="none" stroke="#222" stroke-width="1"/></svg>
    </span>
    <div class="abs search">Search
      <svg width="12" height="12" viewBox="0 0 12 12"><circle cx="5" cy="5" r="3.8" fill="none" stroke="#111" stroke-width="1.6"/><path d="M7.8 7.8 11 11" stroke="#111" stroke-width="1.8"/></svg>
    </div>
  </div>

  <div class="abs brand-name">Veritor</div>
  <div class="abs brand-tag">Real-time reasoning solutions</div>

  <a class="abs btn btn-solid btn-account">Account</a>
  <a class="abs btn btn-login">Log in</a>
  <a class="abs btn btn-signup">Sign up</a>

  <nav class="abs mainnav">
    <a class="active">Home</a>
    <a>Industry</a>
    <a>Telecom</a>
    <a>Power</a>
    <a>Utilities</a>
    <a>Infra</a>
    <a style="border-right:none">Store</a>
  </nav>
</header>

<section>
  <div class="abs hero" role="img" aria-label="Photo of a refinery skyline at sunset reflected in wetland water"></div>
  <div class="abs hero-arrow" style="left:63px">
    <svg width="8" height="10" viewBox="0 0 8 10"><path d="M6 1 2 5 6 9" fill="none" stroke="#222" stroke-width="1.8"/></svg>
  </div>
  <div class="abs hero-arrow" style="left:659px">
    <svg width="8" height="10" viewBox="0 0 8 10"><path d="M2 1 6 5 2 9" fill="none" stroke="#222" stroke-width="1.8"/></svg>
  </div>
</section>

<section>
  <h1 class="abs welcome-title">Welcome to Veritor Website</h1>
  <p class="abs welcome-text">Lorem ipsum dolor sit amet, consectetuer adipiscing elit, sed diam nonummy nibh euismod tincidunt ut laoreet dolore magna aliquam erat volutpat. Ut wisi enim ad minim veniam, quis nostrud exerci tation ullamcorper suscipit lobortis nisl ut aliquip ex ea commodo consequat. Duis autem vel eum iriure dolor in hendrerit in vulputate velit esse molestie consequat, vel illum dolore eu feugiat nulla facilisis at vero eros et accumsan et iusto odio dignissim qui blandit praesent luptatum zzril delenit augue duis dolore te feugait nulla facilisi</p>
  <a class="abs btn btn-solid btn-more">Read More</a>
  <div class="abs divider"></div>
</section>

<section>
  <h2 class="abs clients-title">Our Clients</h2>
  <div class="abs clients">
    <div class="client">Norvane</div>
    <div class="client">Qelta</div>
    <div class="client">Brouwer</div>
    <div class="client">Petrolux</div>
    <div class="client">Seahold</div>
    <div class="client">Dunecor</div>
    <div class="client">Conchera</div>
  </div>

  <div class="abs social-bar">
    <div class="social social-first">Chirp</div>
    <div class="social">Vidly</div>
    <div class="social">Linkr</div>
    <div class="email">Enter you email address</div>
    <div class="subscribe">Subscribe</div>
  </div>
</section>

<footer class="abs footer">
  <div class="abs footer-rule"></div>
  <div class="abs footer-col" style="left:62px"><h3>Solutions</h3>
    <ul><li>KAL Alarm Reporting</li><li>KAL Alarm Analysis</li><li>KAL Alarm Expert</li><li>USE</li></ul></div>
  <div class="abs footer-col" style="left:206px"><h3>Industries</h3>
    <ul><li>Industry</li><li>Telecom</li><li>Power</li><li>Utilities</li><li>Infra</li></ul></div>
  <div class="abs footer-col" style="left:319px"><h3>About us</h3>
    <ul><li>Company</li><li>Overview</li><li>Leadership</li><li>Partners</li><li>Locations</li></ul></div>
  <div class="abs footer-col" style="left:424px"><h3>News</h3>
    <ul><li>Product News</li><li>Partner News</li><li>Events</li><li>Press Releases</li><li>Vacancies</li></ul></div>
  <div class="abs footer-col" style="left:547px"><h3>Contact details</h3>
    <ul><li>Adress Veritor Haarlem</li><li>Telephone : +31 (0)10 555 0142</li><li>Email : info@veritor.com</li><li>Other offices (link to</li><li>locations)</li></ul></div>
  <div class="abs footer-base"></div>
  <p class="abs copyright">(c) 2105 VERITOR.&nbsp; All Reserved &nbsp;&nbsp;&nbsp;&nbsp; Designed &amp; Developed By PixelForge</p>
</footer>

</body>
</html>
```